Kem7Dex Letterhead

Need a new letterhead for my law firm.
IDENTIFYING INFORMATION BELOW:
Ansel T Brightwater III
Attorney at Law
Address: 4832 Tillbury Rd, Ste 250, Dallas, TX 75204
Phone: 866-402-7183
Fax: 469-583-0271
Email: kem@kem7dex.example
Website: www.kem7dex.example

Colors
0054AA
0677BA
7BADD7
CADEEF
E8F1F8

Requirements
Must have
• Logo needs to be on the letterhead, along with identifying information which is included in the project description.

```html
<!DOCTYPE html>
<html lang="en">
<head>
<meta charset="utf-8">
<title>Kem7Dex Letterhead</title>
<link href="https://fonts.googleapis.com/css2?family=Roboto:wght@400;500;700;900&display=swap" rel="stylesheet">
<style>
  :root {
    --blue-deep: #0054AA;
    --blue-mid: #0677BA;
    --blue-soft: #7BADD7;
    --blue-pale: #CADEEF;
    --blue-mist: #E8F1F8;
    --ink: #1c1c1c;
    --ink-muted: #4a4a4a;
    --paper: #ffffff;
    --backdrop: #ecedef;
  }
  * { margin: 0; padding: 0; box-sizing: border-box; }
  html, body {
    width: 1200px; height: 1013px; overflow: hidden;
    background: var(--backdrop);
    font-family: "Roboto", Arial, sans-serif;
  }
  .letterhead {
    position: absolute; left: 265px; top: 26px;
    width: 669px; height: 960px;
    background: var(--paper);
    box-shadow: 0 2px 10px rgba(0,0,0,0.12);
    overflow: hidden;
  }
  .corner-band {
    position: absolute; left: 0; top: 0;
    width: 64px; height: 246px;
    background: linear-gradient(90deg, var(--blue-mid), var(--blue-deep));
  }
  .foot-band {
    position: absolute; right: 0; bottom: 0;
    width: 184px; height: 56px;
    background: linear-gradient(90deg, var(--blue-deep), var(--blue-mid));
  }
  .brand { position: absolute; left: 113px; top: 44px; }
  .brand-name {
    display: flex; align-items: center; gap: 10px;
    font-weight: 900; font-size: 34px; letter-spacing: 1px;
    color: var(--ink); line-height: 1;
  }
  .brand-mark { width: 14px; height: 14px; background: var(--blue-deep); }
  .brand-tagline {
    margin-top: 6px;
    font-size: 14px; font-weight: 500; letter-spacing: 2.6px;
    color: var(--ink-muted); text-transform: uppercase;
  }
  .contact {
    position: absolute; right: 45px; top: 47px;
    padding-right: 12px;
    border-right: 3px solid var(--blue-deep);
    text-align: left; width: 210px;
  }
  .contact-name { font-size: 15px; font-weight: 700; color: var(--ink); }
  .contact-role { font-size: 11px; color: var(--blue-mid); margin-top: 1px; }
  .contact-list { list-style: none; margin-top: 14px; }
  .contact-list li {
    display: flex; align-items: flex-start; gap: 6px;
    font-size: 10px; color: var(--ink-muted); line-height: 14px;
  }
  .contact-list li.gap { margin-top: 8px; }
  .contact-list svg { flex: 0 0 10px; width: 10px; height: 10px; margin-top: 2px; fill: var(--blue-deep); }
</style>
</head>
<body>
  <main class="letterhead">
    <div class="corner-band"></div>

    <header class="brand">
      <div class="brand-name"><span>KEM7DEX</span><span class="brand-mark"></span></div>
      <div class="brand-tagline">Counsel you can count on</div>
    </header>

    <section class="contact">
      <div class="contact-name">Ansel T Brightwater III</div>
      <div class="contact-role">Attorney at Law</div>
      <ul class="contact-list">
        <li>
          <svg viewBox="0 0 10 10"><path d="M5 0a3.5 3.5 0 0 0-3.5 3.5C1.5 6 5 10 5 10s3.5-4 3.5-6.5A3.5 3.5 0 0 0 5 0zm0 5a1.5 1.5 0 1 1 0-3 1.5 1.5 0 0 1 0 3z"/></svg>
          <span>4832 Tillbury Rd, Ste 250,<br>Dallas, TX 75204</span>
        </li>
        <li class="gap">
          <svg viewBox="0 0 10 10"><path d="M2 0.5l2 2-1 1.2c.6 1.3 1.6 2.3 2.9 2.9L7 5.6l2 2-1.3 1.6C4 9 1 6 .5 2.3z"/></svg>
          <span>866-402-7183</span>
        </li>
        <li>
          <svg viewBox="0 0 10 10"><rect x="1" y="3" width="8" height="5" rx="1"/><rect x="3" y="1" width="4" height="2"/></svg>
          <span>469-583-0271</span>
        </li>
        <li>
          <svg viewBox="0 0 10 10"><path d="M0 2h10v6H0z M0 2l5 3.5L10 2" fill="none" stroke="#0054AA" stroke-width="1.2"/></svg>
          <span>kem@kem7dex.example</span>
        </li>
        <li>
          <svg viewBox="0 0 10 10"><circle cx="5" cy="5" r="4.3" fill="none" stroke="#0054AA" stroke-width="1.2"/><path d="M0.7 5h8.6M5 0.7v8.6" stroke="#0054AA" stroke-width="1"/></svg>
          <span>www.kem7dex.example</span>
        </li>
      </ul>
    </section>

    <div class="foot-band"></div>
  </main>
</body>
</html>
```